Business Cards Needed For Veterinary Business

Looking for a business card design for a veterinary blood bank. We would like it to be clean and professional on appearance but still warm and inviting. We would like to utilize our logo and similar coloring. We will use our phone number, email, website, employee name, employee title.

We do not want a bunch of animated animal photos but do not need the style to be as clinical as a laboratory or human medical procedure office.

We are looking for some creative ideas to choose from so that we can generate a standout professional business card for our management team to utilize.

Target Market(s)

professionals

Industry/Entity Type

veterinary

Contact Information for Business Card

employee name, employee title, phone number, website URL, email

Font styles to use
Sans Serif

Colors
0054AA
0677BA
7BADD7
CADEEF
E8F1F8
EB3D1F
EC4F4E
F09395
F8D3D4
FCEDEE

Requirements
Nice to have
• creative design
Should not have
• animated photos

```html
<!DOCTYPE html>
<html lang="en">
<head>
<meta charset="utf-8">
<title>Cedarwell Animal Blood Services – Business Card</title>
<link href="https://fonts.googleapis.com/css2?family=Montserrat:wght@400;500;700;800&display=swap" rel="stylesheet">
<style>
  :root {
    --blue: #0F4F96;
    --red: #EB3D1F;
    --white: #FFFFFF;
    --page: #ECEFF3;
    --scene-teal: #2F7A6E;
    --scene-green: #3E8F78;
    --scene-wood: #8A4A26;
  }
  * { box-sizing: border-box; margin: 0; padding: 0; }
  html, body { width: 1200px; height: 878px; overflow: hidden; }
  body {
    background: var(--page);
    font-family: "Montserrat", Arial, sans-serif;
    position: relative;
  }
  .card {
    position: absolute;
    top: 129px;
    width: 380px;
    height: 620px;
    border-radius: 30px;
    overflow: hidden;
    box-shadow: 0 10px 24px rgba(0,0,0,.18);
    background: var(--blue);
  }
  .card--front { left: 150px; }
  .card--back { left: 670px; }

  /* Front */
  .front-scene {
    position: absolute; left: 0; top: 0; width: 100%; height: 250px;
    background: linear-gradient(160deg, var(--scene-green) 0%, var(--scene-teal) 55%, var(--scene-wood) 100%);
  }
  .front-name {
    position: absolute; left: 30px; right: 30px; top: 250px; bottom: 0;
    display: flex; align-items: center; justify-content: center;
    text-align: center;
    color: var(--white);
    font-size: 34px;
    font-weight: 700;
    line-height: 1.25;
  }

  /* Back */
  .back-top {
    position: absolute; left: 0; top: 0; width: 100%; height: 250px;
    background: var(--white);
  }
  .back-name {
    position: absolute; left: 30px; right: 30px; top: 0; height: 250px;
    display: flex; align-items: center; justify-content: center;
    text-align: center;
    color: var(--red);
    font-size: 30px;
    font-weight: 700;
    line-height: 1.25;
  }
  .person {
    position: absolute; left: 0; right: 0; top: 350px;
    text-align: center; color: var(--white);
  }
  .person__name { font-size: 22px; font-weight: 800; letter-spacing: .5px; }
  .person__title { font-size: 17px; font-weight: 400; margin-top: 4px; }
  .contact-icons {
    position: absolute; left: 0; right: 0; top: 430px;
    display: flex; justify-content: center; gap: 26px;
  }
  .contact-icon {
    width: 28px; height: 28px; border-radius: 50%;
    background: var(--red);
    display: flex; align-items: center; justify-content: center;
  }
  .contact-icon svg { width: 16px; height: 16px; }
  .contact-list {
    position: absolute; left: 0; right: 0; top: 474px;
    list-style: none; text-align: center;
    color: var(--white); font-size: 15px; font-weight: 500; line-height: 1.5;
  }
  .divider {
    position: absolute; left: 60px; right: 60px; top: 546px;
    height: 1px; background: rgba(255,255,255,.75);
  }
  .address {
    position: absolute; left: 0; right: 0; top: 556px;
    text-align: center; color: var(--white);
    font-size: 14px; font-style: normal; line-height: 1.45;
  }
</style>
</head>
<body>

<section class="card card--front" aria-label="Card front">
  <div class="front-scene" role="img" aria-label="Illustration of a veterinarian examining a dog in a clinic"></div>
  <p class="front-name">Cedarwell<br>Animal Blood<br>Services</p>
</section>

<section class="card card--back" aria-label="Card back">
  <div class="back-top"></div>
  <p class="back-name">Cedarwell Animal<br>Blood Services</p>

  <div class="person">
    <p class="person__name">DANIEL BROOKS</p>
    <p class="person__title">Co-Founder &amp; CEO</p>
  </div>

  <div class="contact-icons">
    <span class="contact-icon" aria-label="Phone">
      <svg viewBox="0 0 24 24"><path fill="#fff" d="M6.6 10.8a15.5 15.5 0 0 0 6.6 6.6l2.2-2.2c.3-.3.7-.4 1-.2 1.1.4 2.3.6 3.6.6.6 0 1 .4 1 1V20c0 .6-.4 1-1 1A17 17 0 0 1 3 4c0-.6.4-1 1-1h3.5c.6 0 1 .4 1 1 0 1.3.2 2.5.6 3.6.1.3 0 .7-.2 1z"/></svg>
    </span>
    <span class="contact-icon" aria-label="Email">
      <svg viewBox="0 0 24 24"><rect x="3" y="6" width="18" height="12" rx="1" fill="#fff"/><path d="M3.5 6.5 12 13l8.5-6.5" stroke="#EB3D1F" stroke-width="1.6" fill="none"/></svg>
    </span>
    <span class="contact-icon" aria-label="Website">
      <svg viewBox="0 0 24 24" fill="none" stroke="#fff" stroke-width="1.8"><circle cx="12" cy="12" r="8.5"/><ellipse cx="12" cy="12" rx="3.8" ry="8.5"/><path d="M3.5 12h17"/></svg>
    </span>
  </div>

  <ul class="contact-list">
    <li>555-0142-38271</li>
    <li>info@cedarwellabs.com</li>
    <li>www.cedarwellabs.com</li>
  </ul>
  <div class="divider"></div>
  <address class="address">214 Maple Ridge Lane<br>Fairview, CT 06000 USA</address>
</section>

</body>
</html>
```